Redesign Website Homepage Header

We are looking for a re-design of the header section of our website homepage. The style of the website, image assets and copy can all remain the same, but we want an alternative layout that matches the rest of the website. Full brief attached.

Reason: Project has been launched over a weekend so might have low response. Extending to cover more working week days.

```html
<!DOCTYPE html>
<html lang="en">
<head>
<meta charset="utf-8">
<title>Hosted Desktop for IT Resellers</title>
<link rel="stylesheet" href="https://fonts.googleapis.com/css2?family=Montserrat:wght@300;400;500&display=swap">
<style>
  :root {
    --page-bg: #ffffff;
    --headline: #0b4f7b;
    --lead: #ffffff;
    --hero-light: #dfe6ea;
    --hero-mid: #9fc3d8;
    --hero-deep: #0c5ea6;
    --hero-dark: #1f4a6b;
    --play-bg: #d9d9d9;
    --play-icon: #1d4a68;
  }
  * { margin: 0; padding: 0; box-sizing: border-box; }
  html, body {
    width: 1200px;
    height: 683px;
    overflow: hidden;
    background: var(--page-bg);
    font-family: "Montserrat", Arial, sans-serif;
  }
  .canvas {
    position: relative;
    width: 1200px;
    height: 683px;
    background: var(--page-bg);
  }
  .hero {
    position: absolute;
    left: 0;
    top: 120px;
    width: 1200px;
    height: 459px;
    overflow: hidden;
  }
  .hero-photo {
    position: absolute;
    inset: 0;
    background:
      radial-gradient(ellipse 520px 420px at 120px 459px, var(--hero-deep) 0%, rgba(12,94,166,0.55) 45%, rgba(12,94,166,0) 100%),
      radial-gradient(ellipse 420px 260px at 760px 420px, rgba(31,74,107,0.75) 0%, rgba(31,74,107,0) 100%),
      linear-gradient(180deg, var(--hero-light) 0%, #cfdde6 40%, var(--hero-mid) 100%);
  }
  .hero-content {
    position: absolute;
    inset: 0;
    text-align: center;
  }
  .hero-title {
    position: absolute;
    left: 0;
    right: 0;
    top: 204px;
    color: var(--headline);
    font-weight: 500;
    font-size: 84px;
    line-height: 1;
    letter-spacing: 2px;
    text-shadow: 0 2px 4px rgba(0,0,0,0.15);
  }
  .hero-title .title-main {
    position: absolute;
    left: 0;
    right: 0;
    top: 0;
    transform: translateY(-120px);
  }
  .hero-title .title-sub {
    position: absolute;
    left: 0;
    right: 0;
    top: 0;
    font-weight: 300;
    font-size: 45px;
    letter-spacing: 1.5px;
    transform: translateY(-30px);
  }
  .hero-lead {
    position: absolute;
    left: 0;
    right: 0;
    top: 238px;
    color: var(--lead);
    font-weight: 400;
    font-size: 21px;
    line-height: 25px;
  }
  .play-button {
    position: absolute;
    left: 570px;
    top: 328px;
    width: 60px;
    height: 60px;
  }
</style>
</head>
<body>
  <div class="canvas">
    <section class="hero">
      <div class="hero-photo" role="img" aria-label="Blurred photo of a person working at a desktop computer showing lines of code"></div>
      <div class="hero-content">
        <h1 class="hero-title">
          <span class="title-main">HOSTED DESKTOP</span>
          <span class="title-sub">FOR IT RESELLERS</span>
        </h1>
        <p class="hero-lead">Get more customers, increase margins and grow your business<br>by reselling NimbusDesk virtual hosted desktops.</p>
        <svg class="play-button" viewBox="0 0 60 60" aria-label="Play video">
          <circle cx="30" cy="30" r="30" fill="var(--play-bg)"/>
          <path d="M23 16 L43 30 L23 44 Z" fill="var(--play-icon)"/>
        </svg>
      </div>
    </section>
  </div>
</body>
</html>
```